mno school poster design and change logo name

We already have a logo which only needs to be slightly modified with "school".
We also have two advertising faces, a girl and a boy, which should be on our poster.
Important key data:

bilingual D/E small classes
daycare
private kindergarten
private school from 2024

Poster size: 268,5 x 128 cm
We need logo sizes in different sizes
also for T-shirts.
Attached also a old poster

Target Market(s)

new clients

Colors
0094D4
00A9DD
6FCCEA
C7EBF8
E9F6FB
59FF00
82FF00
B8FF75
E3FFCB
F4FFEA
FFC000
F8CF3A
FAE287
FDF2CF
FEFAEE
F0912C
F2A743
F7CA91
FBE8D2
FDF5EE

```html
<!DOCTYPE html>
<html lang="en">
<head>
<meta charset="utf-8">
<title>mno Schools – Daycare Poster</title>
<link rel="stylesheet" href="https://fonts.googleapis.com/css2?family=Fredoka:wght@600;700&family=Sniglet:wght@400;800&display=swap">
<style>
  :root {
    --page: #e4e5e8;
    --paper: #fafafa;
    --white: #ffffff;
    --purple: #6a5b9e;
    --pink: #e9348a;
    --blue: #1aa9e0;
    --sky: #40c4f5;
    --lime: #b7cc12;
    --orange: #ffae00;
    --sand: #f8cf6a;
    --ink: #111111;
  }
  * { margin: 0; padding: 0; box-sizing: border-box; }
  html, body {
    width: 1200px; height: 800px; overflow: hidden;
    background: var(--page);
  }
  .poster {
    position: absolute; left: 20px; top: 123px;
    width: 1160px; height: 553px;
    background: var(--paper);
    overflow: hidden;
  }
  .decor { position: absolute; inset: 0; }
  .brand-box {
    position: absolute; left: 0; top: 0; width: 300px; height: 246px;
    background: var(--white);
    display: flex; flex-direction: column; align-items: center; justify-content: center; gap: 14px;
  }
  .brand-mark { width: 70px; height: 70px; border-radius: 50%; background: var(--orange); }
  .brand-name {
    font-family: "Sniglet", sans-serif; font-weight: 800;
    font-size: 40px; color: var(--orange); line-height: 1; white-space: nowrap;
  }
  .headline {
    position: absolute; left: 366px; top: 44px;
    font-family: "Fredoka", sans-serif; font-weight: 700;
    font-size: 98px; letter-spacing: 1px; color: var(--purple); line-height: 1;
    white-space: nowrap;
  }
  .features {
    position: absolute; left: 40px; top: 270px; width: 530px; list-style: none;
    font-family: "Sniglet", sans-serif; font-weight: 800; font-size: 33px; line-height: 51px;
    white-space: nowrap;
  }
  .features li { display: flex; align-items: center; }
  .features li::before {
    content: ""; flex: none; width: 15px; height: 15px; border-radius: 50%;
    background: currentColor; margin-right: 13px;
  }
  .features .pink { color: var(--pink); }
  .features .blue { color: var(--blue); }
  .features .lime { color: var(--lime); }
  .photo { position: absolute; border-radius: 50%; }
  .photo-girl {
    left: 867px; top: 31px; width: 246px; height: 246px;
    background: radial-gradient(circle at 50% 45%, #f1cdb4 0%, #c99a72 40%, #e8f4fb 75%);
  }
  .photo-boy {
    left: 664px; top: 199px; width: 272px; height: 272px;
    background: radial-gradient(circle at 55% 35%, #d9a57d 0%, #8a5a3c 35%, #3fb3e0 70%, #ffffff 90%);
  }
  .contact-bar {
    position: absolute; left: 0; bottom: 0; width: 100%; height: 52px;
    background: var(--orange);
    font-family: "Sniglet", sans-serif; font-weight: 800; font-size: 25px; color: var(--ink);
  }
  .contact-item { position: absolute; top: 0; height: 52px; display: flex; align-items: center; gap: 10px; white-space: nowrap; }
  .contact-phone { left: 146px; }
  .contact-web { left: 486px; }
  .social { position: absolute; right: 28px; top: 15px; display: flex; gap: 8px; }
  .social span { width: 23px; height: 23px; border-radius: 50%; border: 2px solid var(--white); }
</style>
</head>
<body>
<main class="poster">
  <svg class="decor" width="1160" height="553" viewBox="0 0 1160 553" aria-hidden="true">
    <g fill="none" stroke-linecap="round" stroke-width="3.5" stroke-dasharray="0 11">
      <line x1="318" y1="4" x2="318" y2="250" stroke="var(--sky)"/>
      <line x1="345" y1="4" x2="345" y2="186" stroke="var(--sky)"/>
      <line x1="604" y1="186" x2="604" y2="498" stroke="var(--sand)"/>
      <line x1="575" y1="389" x2="575" y2="498" stroke="var(--sand)"/>
      <line x1="4" y1="447" x2="224" y2="447" stroke="var(--pink)"/>
      <line x1="83" y1="476" x2="426" y2="476" stroke="var(--pink)"/>
    </g>
    <g fill="var(--sky)">
      <circle cx="450" cy="191" r="4.5"/><circle cx="484" cy="191" r="4.5"/><circle cx="518" cy="191" r="4.5"/>
    </g>
    <g fill="var(--pink)">
      <circle cx="956" cy="476" r="4.5"/><circle cx="990" cy="476" r="4.5"/><circle cx="1025" cy="476" r="4.5"/>
    </g>
    <g fill="none" stroke-linecap="round">
      <path d="M924 14 A155 155 0 0 0 844 207" stroke="var(--pink)" stroke-width="8"/>
      <path d="M1090 35 A155 155 0 0 1 976 308" stroke="var(--pink)" stroke-width="9"/>
      <circle cx="990" cy="154" r="131" stroke="var(--pink)" stroke-width="10"/>
      <path d="M740 170 A176 176 0 0 0 726 494" stroke="var(--sky)" stroke-width="8"/>
      <path d="M965 365 A176 176 0 0 1 924 459" stroke="var(--sky)" stroke-width="4"/>
      <circle cx="800" cy="335" r="147" stroke="var(--sky)" stroke-width="10"/>
      <circle cx="1069" cy="404" r="54" stroke="var(--purple)" stroke-width="3"/>
    </g>
    <circle cx="1069" cy="404" r="42" fill="var(--purple)"/>
  </svg>

  <div class="brand-box">
    <div class="brand-mark"></div>
    <div class="brand-name">mno Schools</div>
  </div>

  <h1 class="headline">DAYCARE</h1>

  <ul class="features">
    <li class="pink">bilingual D/E small classes</li>
    <li class="blue">private kindergarten</li>
    <li class="lime">private school from 2024</li>
  </ul>

  <div class="photo photo-girl" role="img" aria-label="Photo of a smiling girl holding up paint-covered hands"></div>
  <div class="photo photo-boy" role="img" aria-label="Photo of a laughing boy in a blue T-shirt showing colourful painted hands"></div>

  <footer class="contact-bar">
    <div class="contact-item contact-phone">
      <svg width="26" height="28" viewBox="0 0 24 24" aria-hidden="true">
        <path d="M6.6 2.5l3 3.2-1.9 2.6c1 2.6 3.4 5.2 6.2 6.5l2.5-1.9 3.2 3-1.8 3.300c-7.6-.6-13.6-6.8-14-14.600z" fill="var(--ink)"/>
      </svg>
      <span>+41 79 555 01 23</span>
    </div>
    <div class="contact-item contact-web">
      <svg width="30" height="30" viewBox="0 0 24 24" aria-hidden="true" fill="none" stroke="var(--ink)" stroke-width="1.6">
        <circle cx="12" cy="12" r="10"/><ellipse cx="12" cy="12" rx="4.5" ry="10"/>
        <line x1="2" y1="12" x2="22" y2="12"/><path d="M4 6.5h16M4 17.5h16"/>
      </svg>
      <span>www.mno-daycare.ch</span>
    </div>
    <div class="social" aria-hidden="true"><span></span><span></span><span></span><span></span></div>
  </footer>
</main>
</body>
</html>
```